Front cover for our tenth anniversary show programme

To create an eye catching tenth anniversary front cover for our programme

Moonwren presents STRIDE! 2015

date of the show Sunday 3rd May 2015

Venue The Corrimore Playhouse

please see the updated brief!

Reason: there hasn't been anything that is quite right

```html
<!DOCTYPE html>
<html lang="en">
<head>
<meta charset="utf-8">
<title>Moonwren presents STRIDE! 2015 – Programme Cover</title>
<link rel="stylesheet" href="https://fonts.googleapis.com/css2?family=Archivo+Black&family=Great+Vibes&family=Montserrat:wght@700;800&family=Raleway:wght@200;300&display=swap">
<style>
  :root {
    --ink-dark: #2a2a2c;
    --ink-deeper: #1c1c1e;
    --beam: rgba(255,255,255,0.07);
    --neon-pink: #ff2fa8;
    --hot-pink: #e8318f;
    --white: #ffffff;
    --rule: rgba(255,255,255,0.7);
  }
  html, body {
    margin: 0;
    padding: 0;
    overflow: hidden;
    background: var(--ink-deeper);
  }
  .cover {
    position: relative;
    width: 848px;
    height: 1200px;
    overflow: hidden;
    background: radial-gradient(ellipse at 60% 45%, #3a3a3d 0%, var(--ink-dark) 55%, var(--ink-deeper) 100%);
  }
  .cover__art {
    position: absolute;
    inset: 0;
    width: 848px;
    height: 1200px;
  }
  .brand {
    position: absolute;
    top: 255px;
    left: 300px;
    width: 520px;
    text-align: center;
    font-family: "Montserrat", sans-serif;
    font-weight: 800;
    font-size: 92px;
    line-height: 1;
    color: var(--white);
    letter-spacing: -1px;
    text-transform: lowercase;
  }
  .tagline {
    position: absolute;
    left: 340px;
    width: 440px;
    text-align: center;
    font-family: "Montserrat", sans-serif;
    font-weight: 800;
    color: var(--white);
    margin: 0;
  }
  .tagline--celebrating {
    top: 385px;
    font-size: 31px;
  }
  .tagline--years {
    top: 428px;
    font-size: 66px;
    letter-spacing: -1px;
    line-height: 1;
  }
  .tagline--years .accent { color: var(--hot-pink); }
  .presents {
    position: absolute;
    top: 512px;
    left: 340px;
    width: 440px;
    text-align: center;
    font-family: "Great Vibes", cursive;
    font-size: 40px;
    color: var(--white);
    margin: 0;
  }
</style>
</head>
<body>
<main class="cover">
  <svg class="cover__art" viewBox="0 0 848 1200" xmlns="http://www.w3.org/2000/svg">
    <defs>
      <linearGradient id="photo-warm" x1="0" y1="0" x2="1" y2="1">
        <stop offset="0" stop-color="#6b1f3a"/>
        <stop offset="1" stop-color="#241018"/>
      </linearGradient>
      <linearGradient id="photo-cool" x1="0" y1="0" x2="1" y2="1">
        <stop offset="0" stop-color="#2b3040"/>
        <stop offset="0.6" stop-color="#8a3a6a"/>
        <stop offset="1" stop-color="#3a2434"/>
      </linearGradient>
      <linearGradient id="photo-stage" x1="0" y1="0" x2="1" y2="0">
        <stop offset="0" stop-color="#a0203a"/>
        <stop offset="1" stop-color="#3a1030"/>
      </linearGradient>
      <linearGradient id="photo-solo" x1="0" y1="0" x2="0" y2="1">
        <stop offset="0" stop-color="#3a3c6a"/>
        <stop offset="0.5" stop-color="#c9b9b0"/>
        <stop offset="1" stop-color="#8a1a2a"/>
      </linearGradient>
      <filter id="neon-glow" x="-20%" y="-30%" width="140%" height="160%">
        <feGaussianBlur stdDeviation="5" result="blur"/>
        <feMerge><feMergeNode in="blur"/><feMergeNode in="blur"/><feMergeNode in="SourceGraphic"/></feMerge>
      </filter>
    </defs>

    <g class="light-beams">
      <polygon points="330,870 848,120 848,330" fill="var(--beam)"/>
      <polygon points="330,870 848,560 848,700" fill="var(--beam)"/>
      <polygon points="330,870 520,0 700,0" fill="var(--beam)"/>
      <polygon points="330,870 848,980 848,1200 700,1200" fill="var(--beam)"/>
      <polygon points="330,870 180,0 300,0" fill="rgba(255,255,255,0.04)"/>
    </g>

    <g class="photo-collage">
      <polygon role="img" aria-label="Photo collage: dancers performing on stage in dark red light"
               points="0,0 250,0 215,400 0,420" fill="url(#photo-warm)"/>
      <polygon role="img" aria-label="Photo: dance troupe in dark military-style costumes and a line of young dancers in pink"
               points="0,430 225,410 330,415 345,790 0,730" fill="url(#photo-cool)"/>
      <polygon role="img" aria-label="Photo: masked dancer crouching on a red-lit stage"
               points="0,830 300,800 250,1200 0,1200" fill="url(#photo-stage)"/>
      <polygon role="img" aria-label="Photo: young performer in a white blouse singing on stage"
               points="300,800 420,830 540,1200 250,1200" fill="url(#photo-solo)"/>
    </g>

    <g class="show-title" font-family="'Archivo Black', sans-serif" font-size="118" fill="none"
       stroke="var(--neon-pink)" stroke-width="4" filter="url(#neon-glow)">
      <text x="420" y="700" textLength="380" lengthAdjust="spacingAndGlyphs">STRIDE!</text>
      <text x="420" y="802" textLength="380" lengthAdjust="spacingAndGlyphs">2015</text>
    </g>

    <g class="show-details">
      <text class="detail-label" transform="translate(432 930) rotate(-90)"
            font-family="'Montserrat', sans-serif" font-weight="800" font-size="21"
            letter-spacing="3" fill="var(--hot-pink)">VENUE</text>
      <text x="445" y="898" font-family="'Raleway', sans-serif" font-weight="300" font-size="45"
            fill="var(--white)" textLength="345" lengthAdjust="spacingAndGlyphs">THE CORRIMORE</text>
      <text x="445" y="955" font-family="'Raleway', sans-serif" font-weight="300" font-size="52"
            fill="var(--white)" textLength="345" lengthAdjust="spacingAndGlyphs">PLAYHOUSE</text>

      <line x1="425" y1="988" x2="790" y2="988" stroke="var(--rule)" stroke-width="1.5"/>

      <text class="detail-label" transform="translate(432 1100) rotate(-90)"
            font-family="'Montserrat', sans-serif" font-weight="800" font-size="21"
            letter-spacing="3" fill="var(--hot-pink)">DATE</text>
      <text x="445" y="1050" font-family="'Raleway', sans-serif" font-weight="200" font-size="50"
            fill="var(--white)" textLength="345" lengthAdjust="spacing">SUNDAY</text>
      <text x="445" y="1100" font-family="'Raleway', sans-serif" font-weight="300" font-size="46"
            fill="var(--white)" textLength="345" lengthAdjust="spacingAndGlyphs">3RD MAY 2015</text>
    </g>
  </svg>

  <div class="brand">Moonwren</div>
  <p class="tagline tagline--celebrating">Celebrating</p>
  <p class="tagline tagline--years"><span class="accent">Ten</span> Years</p>
  <p class="presents">presents</p>
</main>
</body>
</html>
```